4Star Hotel looking for web design

Hello everyone,
We are located in Cambodia, the hotel should open in 2-3 months. The name will be Velmora-Boutique Hotel. We are looking for a webdesign which is professional, elegant and SIMPLE.
All informations should be easy to find. We are quite open to proposition but we would like to the home page:
-a carousel with around 5-8 picture
-Little menu where we can book a room
By the way, we would like a page for our restaurant, gallery, contact page for description of the rooms. I add some old pictures.
I give an example of what we are expecting:
www.quenrostays.com/tovelspring
We hope that we are proposing a good job for you guys. Have fun and Thanks.
Oh and the winner ( or someone he had choose) of course have free night in our presidential suite
Target Market(s)
We are looking for european Market. Let s say people middle age who are willing to travel in difficult area
Industry/Entity Type
Hotel
Coding
Coded - Design and coding required
Number of Pages Required
5+ page
Requirements
Must have
- Simple, simple and Simple
- Carousel
- place for book a room
- during booking, a menu for select room , and after that another menu for propose like tour in town, taxi, flower, bottle of champagne for example
- during all the process, the customer should be able to know at what step it is and can stop and come back after
- Have to be perfect for smartphone
- Price with drawbar for they know how much they earn with our reduction
Nice to have
- during the process of information (name, adress, tel...), it would be great if they can fill it with a button facebook, google plus, lindkdin, instagram ....
- then a button share on facebook, twitter for know that they book in our hotel
- At the end of the booking, a flashcode with the recapitulatif that customer can scan.

```html
<!DOCTYPE html>
<html lang="en">
<head>
<meta charset="utf-8">
<title>Velmora Boutique Hotel – Blog</title>
<link href="https://fonts.googleapis.com/css2?family=Open+Sans:wght@400;600;700&display=swap" rel="stylesheet">
<style>
:root{
  --brown:#7a2a12;
  --brown-dark:#5e1f0c;
  --orange:#e8891a;
  --orange-light:#f0a43a;
  --text:#555;
  --heading:#333;
  --muted:#999;
  --line:#e3e3e3;
  --light:#f2f2f2;
  --white:#fff;
}
*{box-sizing:border-box;margin:0;padding:0}
html,body{width:768px;height:1200px;overflow:hidden;background:var(--white)}
body{font-family:"Open Sans",Arial,sans-serif;color:var(--text);font-size:10px;position:relative}

.site-header{height:72px;display:flex;align-items:center;justify-content:space-between;padding:0 52px 0 56px}
.brand{display:flex;align-items:center;gap:8px;background:var(--brown);height:72px;padding:0 12px;color:var(--white)}
.brand-mark{width:14px;height:14px;background:var(--orange)}
.brand-name{font-size:12px;font-weight:700;line-height:1.25;width:78px}
.main-nav{display:flex;align-items:center;gap:22px;font-size:10px;font-weight:600;color:var(--heading)}
.main-nav .active{color:var(--orange)}
.search-btn{width:20px;height:20px;border-radius:50%;background:var(--brown-dark);display:flex;align-items:center;justify-content:center}

.hero{position:relative;height:210px;background:linear-gradient(180deg,#b8c4cc 0%,#9aa8ad 40%,#4f6a3c 62%,#2f4a22 100%)}
.hero-banner{position:absolute;left:180px;width:410px;height:30px;background:rgba(232,137,26,.9);color:var(--white);font-size:14px;font-weight:600;letter-spacing:1px;display:flex;align-items:center;justify-content:center}
.hero-banner.one{top:100px;width:300px;left:234px}
.hero-banner.two{top:146px}

.section-title{position:absolute;left:56px;top:294px;width:661px;font-size:12px;font-weight:700;color:var(--heading);padding-bottom:8px;border-bottom:1px solid var(--line)}

.posts{position:absolute;left:56px;top:328px;width:418px}
.post{margin-bottom:38px}
.post-image{height:153px;background:linear-gradient(135deg,#8b5a2b,#c69453 50%,#6b3d1c)}
.post-image.hall{height:146px;background:linear-gradient(90deg,#7a3a1c,#d7b58a 50%,#7a3a1c)}
.post-title{margin-top:16px;font-size:9px;font-weight:700;color:var(--heading)}
.post-meta{margin-top:4px;font-size:7.5px;color:var(--muted)}
.post-meta b{color:var(--heading);font-weight:600}
.post-excerpt{margin-top:8px;font-size:7.5px;line-height:1.55}
.read-more{display:inline-block;margin-top:12px;border:1px solid var(--orange);color:var(--orange);font-size:7px;padding:3px 7px}

.pagination{position:absolute;left:330px;top:964px;display:flex;align-items:center;gap:6px;font-size:8px}
.pagination span{border:1px solid var(--line);padding:3px 6px}
.pagination .current{background:var(--orange);border-color:var(--orange);color:var(--white)}

.sidebar{position:absolute;left:500px;top:328px;width:217px}
.booking{background:var(--brown);padding:12px 16px 16px}
.booking h3{font-size:9px;color:var(--white);font-weight:700;margin-bottom:12px;letter-spacing:.5px}
.field{height:22px;background:var(--white);margin-bottom:8px;display:flex;align-items:center;justify-content:space-between;padding:0 8px;font-size:7.5px;color:var(--muted)}
.field i{width:0;height:0;border-left:4px solid transparent;border-right:4px solid transparent;border-top:5px solid var(--heading)}
.book-btn{margin:12px auto 0;width:80px;height:22px;background:var(--orange);color:var(--white);font-size:8px;font-weight:700;display:flex;align-items:center;justify-content:center}

.widget-title{font-size:10px;font-weight:700;color:var(--heading);margin:34px 0 12px}
.recent{display:flex;gap:8px;margin-bottom:12px}
.recent-thumb{width:34px;height:34px;background:linear-gradient(135deg,#9c6a3a,#d8b07a)}
.recent-text{font-size:7px;line-height:1.4;color:var(--heading)}
.recent-text em{display:block;font-style:normal;color:var(--muted)}
.tags{display:grid;grid-template-columns:1fr 1fr;gap:8px 10px;margin-top:18px}
.tag{border:1px solid var(--line);font-size:7.5px;text-align:center;padding:6px 0;color:var(--text)}

.contact-band{position:absolute;left:0;top:1062px;width:768px;height:98px;background:var(--light);padding:14px 56px}
.contact-band h2{font-size:14px;font-weight:600;color:var(--orange);border-bottom:1px solid #ddd;padding-bottom:6px;width:661px}
.contact-list{display:flex;justify-content:space-between;margin-top:14px;width:661px;font-size:8px}
.contact-item{display:flex;align-items:center;gap:8px;line-height:1.4}

.site-footer{position:absolute;left:0;top:1160px;width:768px;height:40px;background:var(--brown);display:flex;align-items:center;justify-content:space-between;padding:0 40px 0 56px;color:#f1d9c8;font-size:8px}
.social{display:flex;gap:5px}
.social span{width:14px;height:14px;display:block}
.to-top{margin-left:10px;width:16px;height:16px;background:var(--brown-dark);border:1px solid #c9856a}
</style>
</head>
<body>

<header class="site-header">
  <div class="brand"><span class="brand-mark"></span><span class="brand-name">Velmora Boutique Hotel</span></div>
  <nav class="main-nav">
    <span>HOME</span><span>ACCOMMODATION</span><span class="active">BLOG</span><span>FEATURES</span><span>CONTACT US</span>
    <span class="search-btn"><svg width="10" height="10" viewBox="0 0 10 10"><circle cx="4" cy="4" r="3" fill="none" stroke="#fff" stroke-width="1.3"/><line x1="6.2" y1="6.2" x2="9" y2="9" stroke="#fff" stroke-width="1.3"/></svg></span>
  </nav>
</header>

<section class="hero" role="img" aria-label="Wide view over a river with green forest and hotel rooftops">
  <div class="hero-banner one">100 % RESPONSIBLE &amp; MOBILE READY</div>
  <div class="hero-banner two">ROOM AVAILABILITY CHECKER AND BOOKING</div>
</section>

<h1 class="section-title">BLOG</h1>

<main class="posts">
  <article class="post">
    <div class="post-image" role="img" aria-label="Hotel interior with carved wooden wall panels and staircase"></div>
    <h2 class="post-title">LOREM IPSUM DOLOR SIT AMET, CONSECTETUR ADIPISCING ELIT, SED DO EIUSMOD TEMPOR</h2>
    <p class="post-meta">By <b>Admin</b> / 10 September, 2015 / Luxury Hotels / 3 Comments</p>
    <p class="post-excerpt">Lorem ipsum dolor sit amet, consectetur adipiscing elit, sed do eiusmod tempor incididunt ut labore et dolore magna aliqua. Ut enim ad minim veniam, quis nostrud exercitation ullamco laboris nisi ut aliquip ex ea commodo consequat. Duis aute irure dolor in reprehenderit in voluptate velit esse cillum dolore.</p>
    <span class="read-more">READ MORE</span>
  </article>
  <article class="post">
    <div class="post-image hall" role="img" aria-label="Bright hotel corridor with wooden doors and tiled floor"></div>
    <h2 class="post-title">LOREM IPSUM DOLOR SIT AMET, CONSECTETUR ADIPISCING ELIT, SED DO EIUSMOD TEMPOR</h2>
    <p class="post-meta">By <b>Admin</b> / 10 September, 2015 / Luxury Hotels / 3 Comments</p>
    <p class="post-excerpt">Lorem ipsum dolor sit amet, consectetur adipiscing elit, sed do eiusmod tempor incididunt ut labore et dolore magna aliqua. Ut enim ad minim veniam, quis nostrud exercitation ullamco laboris nisi ut aliquip ex ea commodo consequat. Duis aute irure dolor in reprehenderit in voluptate velit esse cillum dolore.</p>
    <span class="read-more">READ MORE</span>
  </article>
</main>

<div class="pagination">Page 1 of 2 <span class="current">1</span><span>2</span><span>»</span></div>

<aside class="sidebar">
  <form class="booking">
    <h3>BOOKING NOW</h3>
    <div class="field">Check In <i></i></div>
    <div class="field">Check Out <i></i></div>
    <div class="field">Rooms <i></i></div>
    <div class="field">Adults <i></i></div>
    <div class="field">Children <i></i></div>
    <div class="field">Room Type <i></i></div>
    <div class="book-btn">BOOK NOW</div>
  </form>

  <h3 class="widget-title">RECENT POSTS</h3>
  <div class="recent"><div class="recent-thumb" role="img" aria-label="Hotel room thumbnail"></div><p class="recent-text">LOREM IPSUM DOLOR SIT AMET, CONSECTETUR ADIPISCING<em>Posted on 7 Sep 2015 by Admin</em></p></div>
  <div class="recent"><div class="recent-thumb" role="img" aria-label="Hotel terrace thumbnail"></div><p class="recent-text">LOREM IPSUM DOLOR SIT AMET, CONSECTETUR ADIPISCING<em>Posted on 7 Sep 2015 by Admin</em></p></div>
  <div class="recent"><div class="recent-thumb" role="img" aria-label="Hotel garden thumbnail"></div><p class="recent-text">LOREM IPSUM DOLOR SIT AMET, CONSECTETUR ADIPISCING<em>Posted on 7 Sep 2015 by Admin</em></p></div>

  <h3 class="widget-title">TAGS</h3>
  <div class="tags">
    <span class="tag">Accommodation</span><span class="tag">Beaches</span>
    <span class="tag">Cities</span><span class="tag">Cocktail Party</span>
    <span class="tag">Fine Dining</span><span class="tag">Hotel</span>
    <span class="tag">Relaxation</span><span class="tag">Resort</span>
    <span class="tag">Luxury</span><span class="tag">Spa</span>
  </div>
</aside>

<section class="contact-band">
  <h2>CONTACT US</h2>
  <div class="contact-list">
    <div class="contact-item"><svg width="12" height="16" viewBox="0 0 12 16"><path d="M6 0C2.7 0 0 2.6 0 5.8 0 10 6 16 6 16s6-6 6-10.2C12 2.6 9.3 0 6 0z" fill="#e8891a"/><circle cx="6" cy="6" r="2.2" fill="#f2f2f2"/></svg><span>1234 Lorem ipsum sit amet, elit<br>Velmora, Cambodia</span></div>
    <div class="contact-item"><svg width="14" height="14" viewBox="0 0 14 14"><path d="M3 1l2 3-1.3 1.5c.8 1.8 2.2 3.2 4 4L9.2 8l3 2-1 2.5C6 12.5 1.5 8 1.5 2.5z" fill="#e8891a"/></svg><span>(123) 456 7890</span></div>
    <div class="contact-item"><svg width="16" height="12" viewBox="0 0 16 12"><rect width="16" height="12" fill="#e8891a"/><path d="M0 0l8 6 8-6" fill="none" stroke="#f2f2f2" stroke-width="1.3"/></svg><span>info@velmora.com</span></div>
    <div class="contact-item"><svg width="14" height="14" viewBox="0 0 14 14"><path d="M3 1l2 3-1.3 1.5c.8 1.8 2.2 3.2 4 4L9.2 8l3 2-1 2.5C6 12.5 1.5 8 1.5 2.5z" fill="#e8891a"/></svg><span>(123) 456 7890</span></div>
  </div>
</section>

<footer class="site-footer">
  <span>Copyright © 2015 Velmora. All rights reserved.</span>
  <div class="social">
    <span style="background:#3b5998"></span><span style="background:#3fa9d8"></span><span style="background:#d24836"></span><span style="background:#e8891a"></span><span style="background:#cc3a3a"></span>
    <span class="to-top"></span>
  </div>
</footer>

</body>
</html>
```